Aesthetic shopify website with functioning mobile version

I need a website that looks aesthetically pleasing using the pictures, logos, and product that I provide in the files. I also need to have an aesthetic easy to use mobile version as well.

Here is a list of things I want included in the website.
- Shipping rates are surfaced during checkout
- Discount codes can be applied in the cart
- A shopper can edit their cart’s content
- There is an option for order status tracking
- An email notification is sent to confirm a purchase

The domain is www.brandelio.com, so I am not sure how to go forward with having you convert it to that domain. I look forward to working with you!

```html
<!DOCTYPE html>
<html lang="en">
<head>
<meta charset="utf-8">
<title>Brandelio – Curl Defining Cream</title>
<link rel="stylesheet" href="https://fonts.googleapis.com/css2?family=Heebo:wght@300;400;500;600;700;800&display=swap">
<style>
:root{
  --ink:#2d2d2d;
  --ink-soft:#333333;
  --gold:#8a7a55;
  --paper:#ffffff;
  --mist:#f7f7f7;
  --photo:#ececec;
  --text:#222222;
  --muted:#5a5a5a;
  --font:'Heebo',sans-serif;
}
*{box-sizing:border-box;margin:0;padding:0}
html,body{width:1200px;height:2809px;overflow:hidden}
body{font-family:var(--font);color:var(--text);background:var(--paper);position:relative}
.abs{position:absolute}

/* hero */
.hero{position:absolute;left:0;top:0;width:1200px;height:785px;background:var(--ink);overflow:hidden}
.hero-watermark{position:absolute;left:122px;top:78px;font:800 200px/1 var(--font);color:var(--ink-soft);letter-spacing:2px;white-space:nowrap}
.hero-portrait{position:absolute;left:600px;top:70px;width:600px;height:640px;
  background:
    linear-gradient(90deg,var(--ink) 0%,rgba(45,45,45,0) 22%),
    linear-gradient(180deg,rgba(45,45,45,0) 70%,rgba(60,58,56,.9) 100%),
    radial-gradient(ellipse 46% 52% at 56% 46%,#c0957b 0%,#9a7260 35%,#5c4a40 65%,#3a3634 85%,var(--ink) 100%)}
.hero-shape{position:absolute;left:0;top:0}
.site-nav{position:absolute;left:0;top:0;width:1200px;height:85px}
.logo{font:800 40px/1 var(--font);color:var(--paper);letter-spacing:1px}
.site-nav .logo{position:absolute;left:101px;top:20px}
.nav-links{list-style:none}
.nav-links li{position:absolute;top:34px;font:500 15px/1 var(--font);color:var(--paper);letter-spacing:.6px;white-space:nowrap}
.nav-icons{position:absolute;left:983px;top:26px}
.cart-count{position:absolute;left:1091px;top:28px;width:13px;height:13px;border-radius:50%;background:var(--gold);font:600 9px/13px var(--font);color:var(--paper);text-align:center}
.hero-copy{position:absolute;left:165px;top:288px;color:var(--paper)}
.hero-kicker{font:400 33px/1 var(--font);letter-spacing:1px}
.hero-title{font:700 43px/1 var(--font);letter-spacing:2px;margin-top:12px}
.hero-sub{font:400 16px/1 var(--font);margin-top:18px}
.hero-cta{position:absolute;left:176px;top:427px;width:150px;height:38px;background:var(--gold)}
.hero-cta span{position:absolute;left:6px;top:6px;width:150px;height:38px;border:1.5px solid var(--paper);font:600 13px/36px var(--font);color:var(--paper);text-align:center;letter-spacing:.5px}
.hero-product{position:absolute;left:430px;top:393px;width:270px;height:305px;border-radius:10px;
  background:radial-gradient(ellipse 60% 55% at 55% 45%,#3e3e3e 0%,#2a2a2a 60%,rgba(45,45,45,0) 100%)}

/* ingredients */
.ingredients h2{position:absolute;left:0;width:1200px;top:802px;text-align:center;font:700 36px/1 var(--font);letter-spacing:2px;color:#111}
.ingredients .lede{position:absolute;left:0;width:1200px;top:856px;text-align:center;font:400 17px/1 var(--font);color:#222}
.ing-photo{position:absolute;left:294px;top:948px;width:431px;height:227px;border-radius:14px;
  background:linear-gradient(90deg,rgba(255,255,255,0) 0%,#d9cfc4 6%,#9a6a55 18%,#5a4038 30%,#3a3a3a 45%,#4a4a4a 70%,#2e2e2e 96%,rgba(255,255,255,0) 100%)}
.ing-icon{position:absolute;width:66px;height:66px;border-radius:50%;background:var(--gold)}
.ing-text{position:absolute;font:400 17px/26.5px var(--font);color:#222}

/* product */
.product{position:absolute;left:0;top:1348px;width:1200px;height:721px;background:var(--mist)}
.prod-photo{position:absolute;left:126px;top:75px;width:467px;height:457px;
  background:radial-gradient(ellipse 30% 44% at 50% 46%,#3a3a3a 0%,#4a4a4a 45%,#9a9a9a 80%,var(--photo) 100%)}
.thumb{position:absolute;top:544px;width:106px;height:98px;
  background:radial-gradient(ellipse 24% 42% at 50% 50%,#333 0%,#555 55%,#fff 100%)}
.prod-info{position:absolute;left:617px;top:64px;width:490px}
.prod-info h1{font:700 38px/1 var(--font);letter-spacing:1.5px;color:#111}
.rating{margin-top:14px;font:400 12px/1 var(--font);color:#222;display:flex;align-items:center;gap:8px}
.stars{color:#e0b400;font-size:13px;letter-spacing:-1px}
.price{margin-top:13px;font:500 13.5px/1 var(--font);display:flex;align-items:center;gap:5px}
.price s{color:#222}
.price b{color:var(--gold);font-weight:500}
.save{border:1px solid var(--gold);color:var(--gold);font-size:9.5px;padding:3px 7px;margin-left:3px}
.desc{margin-top:24px;font:300 13.5px/23px var(--font);color:var(--muted)}
.prod-info h3{margin-top:14px;font:700 15px/1 var(--font);color:#111}
.ing-list{margin-top:8px;font:300 13.5px/23px var(--font);color:var(--muted)}
.qty-label{margin-top:6px;font:400 13px/1 var(--font);color:#444}
.qty{position:absolute;left:618px;top:433px;width:227px;height:53px;border:1.5px solid #222;background:var(--paper);display:flex}
.qty span{flex:0 0 66px;font:700 24px/50px var(--font);text-align:center}
.qty span+span{flex:1;border-left:1.5px solid #222;border-right:1.5px solid #222;font:400 16px/50px var(--font)}
.add-cart{position:absolute;left:865px;top:433px;width:238px;height:53px;background:var(--ink);color:var(--paper);font:600 17px/53px var(--font);text-align:center;letter-spacing:.5px}
.buy-now{position:absolute;left:620px;top:497px;width:483px;height:59px;background:var(--gold);color:var(--paper);font:600 21px/59px var(--font);text-align:center;letter-spacing:1.5px}
.pay-row{position:absolute;display:flex;gap:7px}
.pay-badge{border-radius:4px;background:#e2e2e2}
.secure{position:absolute;left:623px;top:632px;font:400 13.5px/1 var(--font);color:#333}

/* newsletter */
.newsletter{position:absolute;left:0;top:2069px;width:1200px;height:291px;background:var(--gold);overflow:hidden}
.nl-product{position:absolute;left:80px;top:20px;width:230px;height:290px;
  background:radial-gradient(ellipse 48% 60% at 52% 55%,#2e2e2e 0%,#3a3733 55%,rgba(138,122,85,0) 100%)}
.nl-portrait{position:absolute;left:870px;top:0;width:320px;height:291px;
  background:radial-gradient(ellipse 46% 62% at 52% 45%,#a9785f 0%,#7a5844 40%,#8a7a68 70%,rgba(138,122,85,0) 100%)}
.newsletter h2{position:absolute;left:0;width:1200px;top:70px;text-align:center;font:700 35px/39px var(--font);letter-spacing:2px;color:var(--paper)}
.nl-form{position:absolute;left:335px;top:168px;width:487px;height:47px;border:2px solid var(--paper);display:flex}
.nl-form span{flex:1;background:var(--paper);font:400 14px/43px var(--font);color:#444;padding-left:20px}
.nl-form b{width:113px;font:600 14px/43px var(--font);color:var(--paper);text-align:center}

/* footer */
.site-footer{position:absolute;left:0;top:2360px;width:1200px;height:449px;background:var(--ink);color:var(--paper)}
.site-footer .logo{position:absolute;left:0;width:1200px;top:75px;text-align:center;font-size:42px}
.social{position:absolute;top:153px;left:527px;display:flex;gap:17px}
.social i{width:16px;height:16px;border-radius:3px;background:var(--paper)}
.foot-links{list-style:none}
.foot-links li{position:absolute;top:199px;font:400 14px/1 var(--font);letter-spacing:.4px;white-space:nowrap}
.disclaimer{position:absolute;left:215px;width:770px;top:292px;text-align:center;font:400 12px/20.5px var(--font)}
.rule{position:absolute;left:100px;top:397px;width:1000px;height:1px;background:#666}
.copyright{position:absolute;left:103px;top:415px;font:400 14px/1 var(--font)}
.legal{position:absolute;right:100px;top:415px;font:400 14px/1 var(--font)}
</style>
</head>
<body>

<header class="hero">
  <div class="hero-watermark" aria-hidden="true">BRANDELIO</div>
  <div class="hero-portrait" role="img" aria-label="Portrait photo of a man with curly hair"></div>
  <svg class="hero-shape" width="1200" height="785" viewBox="0 0 1200 785" aria-hidden="true">
    <path d="M0,785 L0,708 C160,730 360,728 560,692 C720,662 880,620 1010,575 C1090,550 1160,555 1200,585 L1200,785 Z" fill="#ffffff"/>
  </svg>
  <div class="hero-product" role="img" aria-label="Two tubes of curl defining cream"></div>

  <nav class="site-nav">
    <div class="logo">BRANDELIO</div>
    <ul class="nav-links">
      <li style="left:442px">HOME</li>
      <li style="left:522px">OUR STORY</li>
      <li style="left:642px">SHOP</li>
      <li style="left:717px">TESTIMONIALS</li>
      <li style="left:862px">CONTACT US</li>
    </ul>
    <svg class="nav-icons" width="120" height="34" viewBox="0 0 120 34" fill="none" stroke="#fff" stroke-width="1.8" aria-hidden="true">
      <circle cx="15" cy="9" r="7"/><path d="M3,30 C3,20 27,20 27,30"/>
      <circle cx="59" cy="15" r="10"/><path d="M66,22 L73,29"/>
      <path d="M93,4 L98,4 L102,22 L116,22 L119,10 L100,10"/><circle cx="104" cy="28" r="2"/><circle cx="114" cy="28" r="2"/>
    </svg>
    <div class="cart-count">0</div>
  </nav>

  <div class="hero-copy">
    <p class="hero-kicker">LONGER, THICKER,</p>
    <p class="hero-title">HEALTHIER HAIR</p>
    <p class="hero-sub">New Research Proves Its Possible -</p>
  </div>
  <a class="hero-cta"><span>SHOP BRANDELIO</span></a>
</header>

<section class="ingredients">
  <h2>CURL DEFINING CREAM INGREDIENTS</h2>
  <p class="lede">For Definition and Frizz Control With Jojoba Oil &amp; Sunflower Seed Extract</p>
  <svg class="abs" style="left:0;top:900px" width="1200" height="360" viewBox="0 900 1200 360" fill="none" stroke="var(--gold)" stroke-width="1.2" stroke-dasharray="3 2" aria-hidden="true">
    <path d="M625,985 L722,922 L780,955"/>
    <path d="M248,1182 L268,1125 L375,1115"/>
    <path d="M605,1160 L620,1215 L738,1243"/>
  </svg>
  <div class="ing-photo" role="img" aria-label="Tube of curl defining cream lying beside jojoba seeds and leaves"></div>

  <div class="ing-icon" style="left:767px;top:950px"></div>
  <svg class="abs" style="left:767px;top:950px" width="66" height="66" viewBox="0 0 66 66" fill="none" stroke="#fff" stroke-width="1.6" aria-hidden="true">
    <circle cx="33" cy="31" r="8"/><circle cx="33" cy="31" r="14" stroke-dasharray="3 3"/><path d="M33,45 L33,56 M33,52 L27,48 M33,52 L39,48"/>
  </svg>
  <p class="ing-text" style="left:780px;top:1025px;width:320px">Helianthus Annuus (Sunflower) Extract - Naturally-derived UV protectant for hair to prevent color fading, while also conditioning hair and adding shine</p>

  <div class="ing-icon" style="left:206px;top:1188px"></div>
  <svg class="abs" style="left:206px;top:1188px" width="66" height="66" viewBox="0 0 66 66" fill="#fff" aria-hidden="true">
    <ellipse cx="24" cy="24" rx="5" ry="4"/><ellipse cx="40" cy="22" rx="4" ry="5"/><ellipse cx="33" cy="34" rx="5" ry="4"/><ellipse cx="22" cy="42" rx="4" ry="5"/><ellipse cx="43" cy="42" rx="5" ry="4"/>
  </svg>
  <p class="ing-text" style="left:280px;top:1180px;width:300px">Simmondsia Chinensis (Jojoba) Seed Oil - Deep penetrating oil that softens and conditions</p>

  <div class="ing-icon" style="left:738px;top:1192px"></div>
  <svg class="abs" style="left:738px;top:1192px" width="66" height="66" viewBox="0 0 66 66" fill="none" stroke="#fff" stroke-width="2" aria-hidden="true">
    <path d="M20,50 C16,36 20,16 33,16 C46,16 50,36 46,50 M27,50 L27,42 C27,34 39,34 39,42 L39,50"/>
  </svg>
  <p class="ing-text" style="left:815px;top:1192px;width:290px">Polyquaternium-11 - Plant- derived polymer to add volume and help thicken hair</p>
</section>

<section class="product">
  <div class="prod-photo" role="img" aria-label="Product photo of the curl defining cream tube"></div>
  <div class="thumb" style="left:126px" role="img" aria-label="Tube thumbnail, front"></div>
  <div class="thumb" style="left:246px" role="img" aria-label="Tube thumbnail, side"></div>
  <div class="thumb" style="left:367px" role="img" aria-label="Tube thumbnail, back"></div>
  <div class="thumb" style="left:485px" role="img" aria-label="Tube thumbnail, angled"></div>

  <div class="prod-info">
    <h1>BRANDELIO</h1>
    <div class="rating"><span class="stars">★★★★★</span><span>(25) reviews</span></div>
    <div class="price"><s>$150.00</s><b>$110.00</b><span class="save">Save $40</span></div>
    <p class="desc">This amplifying cream defines and separates while adding volume, shine and texture. Retains curl and reduces frizz for a radiant, touchable finish.</p>
    <h3>INGREDIENTS</h3>
    <p class="ing-list">Water/Aqua/Eau, Cyclotetrasiloxane, Polyquaternium-37, Glycerin, VP/DMAPA Acrylates Copolymer, C12-15 Alkyl Benzoate, Propylene Glycol Dicaprylate/Dicaprate, Polyquaternium-11, Fragrance/Parfum, Simmondsia Chinensis (Jojoba) Seed Oil, Polysorbate 60, Cetearyl Alcohol, PPG-1 Trideceth-6, Butylene Glycol, Helianthus Annuus (Sunflower) Seed Extract, Methylisothiazolinone</p>
    <p class="qty-label">Quantity</p>
  </div>
  <div class="qty"><span>+</span><span>1</span><span>−</span></div>
  <div class="add-cart">
    <svg width="18" height="15" viewBox="0 0 18 15" style="vertical-align:-1px;margin-right:6px" fill="#fff" aria-hidden="true"><path d="M0,0 L3,0 L5,9 L15,9 L18,2 L4,2 Z"/><circle cx="6" cy="13" r="1.6"/><circle cx="14" cy="13" r="1.6"/></svg>ADD TO CART
  </div>
  <div class="buy-now">BUY NOW</div>
  <div class="pay-row" style="left:624px;top:577px">
    <i class="pay-badge" style="width:64px;height:42px"></i>
    <i class="pay-badge" style="width:64px;height:42px"></i>
    <i class="pay-badge" style="width:64px;height:42px"></i>
    <i class="pay-badge" style="width:64px;height:42px"></i>
    <i class="pay-badge" style="width:64px;height:42px"></i>
  </div>
  <p class="secure">Guaranteed safe &amp; Secure Checkout</p>
</section>

<section class="newsletter">
  <div class="nl-product" role="img" aria-label="Tilted tube of curl defining cream"></div>
  <div class="nl-portrait" role="img" aria-label="Photo of a smiling woman with curly hair"></div>
  <h2>SUBSCRIBE NEWSLETTER<br>&amp; GET 10% OFF</h2>
  <div class="nl-form"><span>Enter email</span><b>SUBSCRIBE</b></div>
</section>

<footer class="site-footer">
  <div class="logo">BRANDELIO</div>
  <div class="social"><i></i><i></i><i></i><i></i><i></i></div>
  <ul class="foot-links">
    <li style="left:172px">SHOP</li>
    <li style="left:249px">HAIR EXPERTISE</li>
    <li style="left:400px">OUR STORY</li>
    <li style="left:519px">TESTIMONIALS</li>
    <li style="left:661px">REWARDS</li>
    <li style="left:771px">PRESS</li>
    <li style="left:858px">BLOG</li>
    <li style="left:936px">FIND A STORE</li>
  </ul>
  <div class="pay-row" style="left:487px;top:245px;gap:4px">
    <i class="pay-badge" style="width:42px;height:24px;background:#d9d9d9"></i>
    <i class="pay-badge" style="width:42px;height:24px;background:#d9d9d9"></i>
    <i class="pay-badge" style="width:42px;height:24px;background:#d9d9d9"></i>
    <i class="pay-badge" style="width:42px;height:24px;background:#d9d9d9"></i>
    <i class="pay-badge" style="width:42px;height:24px;background:#d9d9d9"></i>
  </div>
  <p class="disclaimer">*DISCLAIMER: Sed ut perspiciatis unde omnis iste natus error sit voluptatem accusantium doloremque laudantium, totam rem aperiam, eaque os qui ratione voluptatem sequi nesciunt. Neque*Disclaimer: Sed ut perspiciatis unde omnis iste natus error sit voluptatem accusipsa quae ab illo inventore veritatis et quasi architecto beatae vitae dicta sunt explicabo. Nemo enim ipsam voluptatem quia voluptas sit aspernat ur aut odit aut fugit, sed quia consequuntur magni dolores eos qui ratione voluptatem sequi nesciunt. Neque</p>
  <div class="rule"></div>
  <p class="copyright">© 2021 Brandelio. All Rights Reserved.</p>
  <p class="legal">Privacy &nbsp;|&nbsp; Terms &nbsp;|&nbsp; Disclaimer</p>
</footer>

</body>
</html>
```